BQL Groundworks & Freight Business Card

Can you please design a business card for an Earthworks, Haulage truck and machinery hire company. They also provide sand soil and mulch supply, as well as screening of products. Can you re-create the logo from the attached but add BQL Groundworks & Freight just use the three diamond design.

Target Market(s)

Earthmoving and Transport, Landscapers, Construction

Contact Information for Business Card

ABN 52 907 334 816, Doug Pelham, Managing Director, BQL Groundworks & Freight Mobile 0438 256 904 Email bqlfreight2010@mailvane.net

Font styles to use
Sans Serif

Colors
ec1f27
000000
cbcbcb
ffffff

Requirements
Must have
• Listed on the back, Earthworks | Haulage | Truck and Machinery Hire | Sand, Soil & Mulch Supply | Screening of Products
Nice to have
• Would be good for it to look appealing to a mans man, because it relates to heavy machinery, earthworks, construction etc. Black, red and white would be good maybe with a bit of silver somewhere.
Should not have
• not sure

```html
<!DOCTYPE html>
<html lang="en">
<head>
<meta charset="utf-8">
<title>BQL Groundworks &amp; Freight – Business Card</title>
<link href="https://fonts.googleapis.com/css2?family=Roboto:wght@400;500;700&family=Roboto+Condensed:wght@500;700&display=swap" rel="stylesheet">
<style>
  :root {
    --stage: #2b2b2b;
    --card-dark: #000000;
    --card-light: #e9e9e9;
    --ink: #111111;
    --ink-soft: #2a2a2a;
    --silver: #8a8a8a;
    --silver-dim: #4a4a4a;
    --accent: #ec1f27;
  }
  * { box-sizing: border-box; margin: 0; padding: 0; }
  html, body { width: 1200px; height: 1200px; overflow: hidden; }
  body {
    background: var(--stage);
    font-family: "Roboto", Arial, sans-serif;
    position: relative;
  }
  .card {
    position: absolute;
    left: 160px;
    width: 880px;
    height: 500px;
    overflow: hidden;
  }
  .card--back { top: 60px; background: var(--card-dark); }
  .card--front { top: 640px; background: var(--card-light); color: var(--ink); }

  /* back */
  .back-brand {
    position: absolute;
    top: 200px; left: 0; right: 0;
    display: flex; justify-content: center; align-items: center; gap: 16px;
  }
  .back-brand__mark { width: 24px; height: 24px; background: var(--accent); }
  .back-brand__name {
    font-weight: 700;
    font-size: 44px;
    letter-spacing: 1px;
    color: var(--silver-dim);
  }
  .back-abn {
    position: absolute;
    bottom: 62px; left: 0; right: 0;
    text-align: center;
    font-weight: 500;
    font-size: 22px;
    letter-spacing: 3px;
    color: var(--silver-dim);
  }

  /* front */
  .front-brand {
    position: absolute;
    top: 70px; right: 60px;
    display: flex; align-items: center; gap: 14px;
  }
  .front-brand__mark { width: 22px; height: 22px; background: var(--accent); }
  .front-brand__name {
    font-weight: 700;
    font-size: 32px;
    letter-spacing: 1px;
    color: var(--ink-soft);
  }
  .person { position: absolute; left: 60px; top: 190px; }
  .person__name { font-weight: 700; font-size: 40px; letter-spacing: -0.5px; line-height: 1.1; }
  .person__role { font-size: 20px; margin-top: 2px; }
  .divider {
    position: absolute;
    left: 0; right: 0; top: 264px;
    height: 3px; background: var(--ink);
  }
  .services {
    position: absolute; right: 60px;
    font-family: "Roboto Condensed", Arial, sans-serif;
    font-weight: 700; font-size: 22px; text-align: right; line-height: 1.2;
  }
  .services--top { top: 230px; }
  .services--bottom { top: 276px; }
  .contacts { position: absolute; left: 70px; top: 310px; list-style: none; }
  .contact { display: flex; align-items: flex-start; gap: 18px; margin-bottom: 8px; }
  .contact__icon {
    width: 40px; height: 40px; border: 2px solid var(--ink);
    display: flex; align-items: center; justify-content: center; flex-shrink: 0;
  }
  .contact__text { font-weight: 700; font-size: 21px; line-height: 1.2; padding-top: 8px; }
  .contact__text--upper { text-transform: uppercase; font-size: 20px; padding-top: 0; }
</style>
</head>
<body>

<section class="card card--back" aria-label="Card back">
  <div class="back-brand">
    <span class="back-brand__mark"></span>
    <span class="back-brand__name">BQL Groundworks &amp; Freight</span>
  </div>
  <div class="back-abn">ABN 52 907 334 816</div>
</section>

<section class="card card--front" aria-label="Card front">
  <div class="front-brand">
    <span class="front-brand__mark"></span>
    <span class="front-brand__name">BQL Groundworks &amp; Freight</span>
  </div>

  <div class="person">
    <div class="person__name">Doug Pelham</div>
    <div class="person__role">Managing Director</div>
  </div>

  <div class="services services--top">Earthworks | Haulage | Truck and Machinery Hire |</div>
  <div class="divider"></div>
  <div class="services services--bottom">Sand, Soil &amp; Mulch Supply | Screening of Products</div>

  <ul class="contacts">
    <li class="contact">
      <span class="contact__icon">
        <svg width="26" height="24" viewBox="0 0 26 24" fill="none" stroke="#111" stroke-width="2">
          <path d="M2 12 L13 3 L24 12"/><path d="M5 10 V22 H21 V10"/><rect x="10" y="14" width="6" height="8"/>
        </svg>
      </span>
      <span class="contact__text contact__text--upper">27 Tolley Street<br>Haverton 6029<br>Perth, WA</span>
    </li>
    <li class="contact">
      <span class="contact__icon">
        <svg width="26" height="24" viewBox="0 0 26 24" fill="none" stroke="#111" stroke-width="2">
          <path d="M3 9 Q13 1 23 9 L20 12 L17 9 H9 L6 12 Z"/><rect x="5" y="13" width="16" height="9" rx="2"/><circle cx="13" cy="17.5" r="2.5"/>
        </svg>
      </span>
      <span class="contact__text">0438 256 904</span>
    </li>
    <li class="contact">
      <span class="contact__icon">
        <svg width="26" height="20" viewBox="0 0 26 20" fill="none" stroke="#111" stroke-width="2">
          <rect x="2" y="2" width="22" height="16"/><path d="M2 2 L13 11 L24 2"/>
        </svg>
      </span>
      <span class="contact__text">bqlfreight2010@mailvane.net</span>
    </li>
  </ul>
</section>

</body>
</html>
```